Premium Landcaping Vehicle Design; for 7 vehicles.

Goal: Designs for all of our landscaping vehicles that are bold, premium, visually appealing, and effectively communicate our brand/service while being practical for a vehicle and the damage it could potentially get from tools etc.
1. Brand Identity:
Logo: Feature our logo prominently but ensure it doesn’t overwhelm the design. It should be visible from a distance.
2. Layout:
Simplicity: The car wrap should not be overcrowded. Less is more in mobile advertising since people have only seconds to take it in.
Flow: Make sure the design flows with the curves and shape of the vehicle, using lines that move smoothly over the contours.
Small truck
Large Truck
Halvek Strider
Small trailer
Dakro Truck
Plant Trailer
Boxtop trailer
Thank you for all the great ideas/ designs. After look at them all. I thought it would be great to see the ute strider have less colour; make it more of a premium look by trying the primary logo on one door and another design over both doors to make it stand out.
The truck - we don't want any block colour over the whole tray of the truck, just the bottom part of this, please. No need for website on the cars, ideally we would prefer Marnovista and contact number to stand out.
Would also be great to see the body of the truck (sides only) all in green; making the colour fade down from the top of the door to the bottom/ near the wheel? So the whole side is green.
Went on vacation/holiday
Hi all,
I have attached our AI logo's to ensure we're seeing the correct logo on the designs; meaning font, size of the wording etc. Would be great to see the correct logo on the design.
Thank you

```html
<!DOCTYPE html>
<html lang="en">
<head>
<meta charset="utf-8">
<title>Marnovista Landscapes – Trailer Signage</title>
<link href="https://fonts.googleapis.com/css2?family=Montserrat:wght@400;500;700&display=swap" rel="stylesheet">
<style>
  :root {
    --forest: #0f3b32;
    --forest-deep: #0a2e27;
    --paper: #f1f1f1;
    --white: #ffffff;
    --ink: #111111;
    --backdrop: #e6e8e7;
  }
  * { margin: 0; padding: 0; box-sizing: border-box; }
  html, body { width: 1200px; height: 3599px; overflow: hidden; background: var(--backdrop); }
  body { font-family: "Montserrat", sans-serif; position: relative; }

  .panel { position: absolute; left: 100px; width: 1000px; overflow: hidden; box-shadow: 0 6px 24px rgba(0,0,0,.12); }
  .panel svg.panel-art { position: absolute; inset: 0; width: 100%; height: 100%; display: block; }

  .side-panel { height: 320px; }
  .side-panel--kerb { top: 420px; }
  .side-panel--road { top: 1400px; }

  .brand-block { position: absolute; top: 70px; color: var(--white); text-align: center; width: 440px; }
  .side-panel--road .brand-block { left: 40px; }
  .side-panel--kerb .brand-block { right: 40px; }
  .brand-mark { width: 46px; height: 46px; border: 4px solid var(--white); margin: 0 auto 22px; }
  .brand-name { font-size: 52px; font-weight: 500; letter-spacing: 6px; line-height: 1; }
  .brand-descriptor { font-size: 18px; font-weight: 500; letter-spacing: 7px; margin-top: 14px; }
  .brand-tagline { font-size: 16px; font-weight: 500; letter-spacing: 2px; margin-top: 16px; }

  .rear-panel { top: 2480px; height: 400px; background: var(--forest); }
  .rear-brand { position: absolute; top: 80px; left: 0; right: 0; display: flex; align-items: center; justify-content: center; gap: 34px; color: var(--white); }
  .rear-brand .brand-mark { margin: 0; width: 70px; height: 70px; border-width: 6px; }
  .rear-brand .brand-text { text-align: right; }
  .rear-brand .brand-name { font-size: 78px; letter-spacing: 9px; }
  .rear-brand .brand-descriptor { font-size: 26px; letter-spacing: 9px; margin-top: 10px; }
  .contact-line { position: absolute; bottom: 34px; left: 0; right: 0; text-align: center; font-size: 36px; font-weight: 700; color: var(--ink); letter-spacing: .5px; }
  .contact-line .divider { font-weight: 400; margin: 0 14px; }
</style>
</head>
<body>

  <!-- Kerb-side panel: brand on the right -->
  <section class="panel side-panel side-panel--kerb">
    <svg class="panel-art" viewBox="0 0 1000 320" preserveAspectRatio="none" aria-hidden="true">
      <rect width="1000" height="320" fill="var(--forest)"/>
      <path d="M0 0 L480 0 C440 150 330 250 0 262 Z" fill="var(--paper)"/>
      <path d="M0 284 C360 272 470 180 505 70 C480 200 360 292 0 298 Z" fill="var(--white)"/>
    </svg>
    <div class="brand-block">
      <div class="brand-mark"></div>
      <div class="brand-name">MARNOVISTA</div>
      <div class="brand-descriptor">LANDSCAPES</div>
      <div class="brand-tagline">DESIGN. CONSTRUCT. MAINTAIN.</div>
    </div>
  </section>

  <!-- Road-side panel: brand on the left -->
  <section class="panel side-panel side-panel--road">
    <svg class="panel-art" viewBox="0 0 1000 320" preserveAspectRatio="none" aria-hidden="true">
      <rect width="1000" height="320" fill="var(--forest)"/>
      <path d="M520 0 L1000 0 L1000 262 C670 250 560 150 520 0 Z" fill="var(--paper)"/>
      <path d="M1000 284 C640 272 530 180 495 70 C520 200 640 292 1000 298 Z" fill="var(--white)"/>
    </svg>
    <div class="brand-block">
      <div class="brand-mark"></div>
      <div class="brand-name">MARNOVISTA</div>
      <div class="brand-descriptor">LANDSCAPES</div>
      <div class="brand-tagline">DESIGN. CONSTRUCT. MAINTAIN.</div>
    </div>
  </section>

  <!-- Rear panel: brand and contact -->
  <section class="panel rear-panel">
    <svg class="panel-art" viewBox="0 0 1000 400" preserveAspectRatio="none" aria-hidden="true">
      <rect width="1000" height="400" fill="var(--forest)"/>
      <path d="M40 282 L960 282 L1000 400 L0 400 Z" fill="var(--paper)"/>
    </svg>
    <div class="rear-brand">
      <div class="brand-mark"></div>
      <div class="brand-text">
        <div class="brand-name">MARNOVISTA</div>
        <div class="brand-descriptor">LANDSCAPES</div>
      </div>
    </div>
    <div class="contact-line">1234-567-890<span class="divider">|</span>mail@marnovista.com</div>
  </section>

</body>
</html>
```